Brochure Design Project - simple web landing page design

we are looking for a simple web landing page - just an online brochure - i have attached a power point for content and thoughts

thanks gilda

Reason: starting to get some good one and thought i would give respondants a day to have another try

```html
<!DOCTYPE html>
<html lang="en">
<head>
<meta charset="utf-8">
<title>Brightfield-IT Solutions</title>
<link rel="stylesheet" href="https://fonts.googleapis.com/css2?family=Arimo:wght@400;700&display=swap">
<style>
  :root {
    --bg-glow: #5b2a5f;
    --bg-mid: #3a1a3d;
    --bg-edge: #140a15;
    --panel-light: #ececec;
    --panel-mid: #d6d6d6;
    --panel-dark: #c4c4c4;
    --item-text: #5f5f5f;
    --white: #ffffff;
    --email-text: #d4d4d4;
    --field-bg: #4f4f4f;
    --field-text: #b8b8b8;
    --accent: #ff6600;
    --button-dark: #0a0a0a;
  }
  * { box-sizing: border-box; margin: 0; padding: 0; }
  html, body { width: 1200px; height: 932px; overflow: hidden; }
  body {
    font-family: "Arimo", Arial, sans-serif;
    background: radial-gradient(ellipse 900px 650px at 720px 250px, var(--bg-glow) 0%, var(--bg-mid) 45%, var(--bg-edge) 100%);
    position: relative;
    color: var(--white);
  }
  .site-title {
    position: absolute; left: 0; width: 1200px; top: 42px;
    text-align: center; font-size: 60px; font-weight: 400; line-height: 1;
  }
  .section-label {
    position: absolute; left: 77px; top: 110px;
    font-size: 45px; font-weight: 400; line-height: 1;
  }
  .social-follow {
    position: absolute; right: 78px; top: 126px;
    display: flex; align-items: center; gap: 8px;
    font-size: 20px;
  }
  .social-follow .mark {
    width: 18px; height: 18px; background: var(--white); border-radius: 3px;
  }
  .panel {
    position: absolute; left: 78px; top: 166px; width: 1044px; height: 599px;
    overflow: hidden;
  }
  .panel-backdrop {
    position: absolute; inset: 0;
    background:
      radial-gradient(ellipse 500px 300px at 820px 180px, rgba(255,255,255,0.7), transparent 70%),
      radial-gradient(ellipse 700px 250px at 700px 520px, rgba(255,255,255,0.35), transparent 70%),
      linear-gradient(160deg, var(--panel-mid) 0%, var(--panel-light) 55%, var(--panel-dark) 100%);
  }
  .service-list { position: absolute; left: 30px; top: 66px; list-style: none; }
  .service-item {
    position: relative; height: 60px; display: flex; align-items: center;
    font-size: 36px; color: var(--item-text);
  }
  .service-item .bullet {
    width: 24px; height: 24px; border-radius: 50%; margin-right: 20px;
    background: radial-gradient(circle at 40% 30%, #d0d0d0 0%, #5a5a5a 45%, #1e1e1e 100%);
  }
  .service-item + .service-item::before {
    content: ""; position: absolute; left: 20px; top: -2px; width: 570px; height: 4px;
    background: linear-gradient(90deg, transparent, #8a8a8a 40%, #8a8a8a 70%, transparent);
  }
  .panel-rule {
    position: absolute; left: 87px; top: 392px; width: 900px; height: 5px;
    background: linear-gradient(90deg, transparent, #a6a6a6 30%, #a6a6a6 75%, transparent);
  }
  .notify-button {
    position: absolute; left: 819px; top: 412px; width: 186px; height: 37px;
    border-radius: 19px; background: linear-gradient(180deg, #4a4a4a 0%, var(--button-dark) 50%, #000 100%);
    border: 2px solid #777; color: var(--white); font-size: 25px;
    display: flex; align-items: center; justify-content: center;
    box-shadow: 0 4px 8px rgba(0,0,0,0.4);
  }
  .signup-form { position: absolute; left: 49px; top: 482px; display: flex; gap: 8px; }
  .email-field {
    width: 290px; height: 36px; border-radius: 7px; background: var(--field-bg);
    color: var(--field-text); font-size: 15px; padding-left: 13px;
    display: flex; align-items: center;
  }
  .signup-button {
    width: 73px; height: 36px; border-radius: 7px; background: var(--accent);
    color: var(--white); font-size: 16px;
    display: flex; align-items: center; justify-content: center;
  }
  .contact-line {
    position: absolute; top: 783px; left: 88px; font-size: 25px; white-space: pre;
  }
  .contact-line .phone { position: absolute; top: 0; }
  .email-address {
    position: absolute; top: 862px; font-size: 22px; color: var(--email-text);
  }
</style>
</head>
<body>
  <h1 class="site-title">Brightfield-IT Solutions</h1>
  <div class="section-label">Incubate</div>
  <div class="social-follow"><span class="mark"></span><span>Follow</span></div>

  <main class="panel">
    <div class="panel-backdrop" role="img" aria-label="Soft grey abstract light-swirl background"></div>
    <ul class="service-list">
      <li class="service-item"><span class="bullet"></span>Business Web Integration</li>
      <li class="service-item"><span class="bullet"></span>Application Development</li>
      <li class="service-item"><span class="bullet"></span>Orvane Technology</li>
      <li class="service-item"><span class="bullet"></span>Technology Start Ups</li>
    </ul>
    <div class="panel-rule"></div>
    <div class="notify-button">Notify Me!</div>
    <div class="signup-form">
      <div class="email-field">Enter your email address...</div>
      <div class="signup-button">Sign Up</div>
    </div>
  </main>

  <div class="contact-line">Contact:  Level 3, 17 Harlow St East Perth WA<span class="phone" style="left:629px">+618 9000 4127</span><span class="phone" style="left:862px">0400 562 913</span></div>
  <div class="email-address" style="left:54px">gilda@brightfield-group.com.au</div>
  <div class="email-address" style="left:487px">marco@brightfield-group.com.au</div>
</body>
</html>
```